Wealth Education Business Needs Sharp Business Card Design

We need a business card design for a recently launched investor education business called Harbor Crest.

The final design should promote security, empowerment, self improvement and financial gain. The card will ideally promote the stature of the business.

For more information and colours please visit harborcrest.com.au

Target Market(s)

Corporate executives and high net worth individuals

Industry/Entity Type

Education

Contact Information for Business Card

Name
Position
Contact Address
Phone
Mobile
Email
Website

```html
<!DOCTYPE html>
<html lang="en">
<head>
<meta charset="utf-8">
<title>Harbor Crest – Business Card</title>
<link rel="stylesheet" href="https://fonts.googleapis.com/css2?family=Josefin+Sans:wght@400&family=Lato:wght@400;700;900&display=swap">
<style>
  :root {
    --bg: #e4e4e4;
    --card-white: #fbfbfa;
    --ink: #3b3b3d;
    --text-dark: #1f2a30;
    --teal: #138a8c;
    --teal-card: #0c9b9c;
    --teal-card-deep: #087f82;
    --green: #7ba43c;
    --blue: #3795d1;
    --outline: #111;
  }
  * { box-sizing: border-box; margin: 0; padding: 0; }
  html, body { width: 1200px; height: 720px; overflow: hidden; }
  body { background: var(--bg); position: relative; font-family: "Lato", sans-serif; }

  .card {
    position: absolute;
    top: 241px;
    width: 419px;
    height: 239px;
    border-radius: 14px;
    overflow: hidden;
  }
  .card--front { left: 148px; background: var(--card-white); }
  .card--back {
    left: 633px;
    background: linear-gradient(135deg, var(--teal-card) 0%, var(--teal-card-deep) 100%);
  }

  .wordmark {
    position: absolute;
    font-family: "Josefin Sans", sans-serif;
    font-weight: 400;
    color: var(--ink);
    letter-spacing: 0.16em;
    white-space: nowrap;
    display: flex;
    align-items: center;
    gap: 14px;
  }
  .wordmark__dot {
    width: 14px; height: 14px; border-radius: 50%;
    background: var(--ink);
    flex: none;
  }
  .card--front .wordmark { left: 18px; top: 38px; font-size: 38px; }
  .card--back .wordmark {
    left: 0; right: 0; top: 102px; justify-content: center;
    font-size: 33px;
  }

  .holder { position: absolute; right: 22px; top: 91px; text-align: right; }
  .holder__name { color: var(--teal); font-weight: 900; font-size: 17px; line-height: 20px; }
  .holder__role { color: var(--text-dark); font-weight: 700; font-size: 11.5px; line-height: 16px; }

  .contact-frame {
    position: absolute;
    left: -4px; top: 129px;
    width: 234px; height: 93px;
    border: 2px solid var(--outline);
    border-radius: 0 14px 14px 0;
  }
  .contact-panel {
    position: absolute;
    left: 0; top: 133px;
    width: 224px; height: 82px;
    background: var(--green);
    border-radius: 0 12px 12px 0;
    padding: 10px 0 0 16px;
  }
  .contact-list { list-style: none; }
  .contact-list li {
    display: flex; align-items: center; gap: 5px;
    font-size: 12px; line-height: 14.6px; color: var(--text-dark);
  }
  .contact-list svg { width: 10px; height: 10px; flex: none; }

  .address-band {
    position: absolute;
    left: 232px; top: 139px;
    width: 187px; height: 71px;
    background: var(--blue);
    padding: 25px 0 0 0;
  }
  .address {
    position: absolute; right: 32px; top: 26px;
    text-align: right; font-size: 12px; line-height: 15px; color: var(--text-dark);
    font-style: normal;
  }
  .address-band svg { position: absolute; right: 17px; top: 28px; width: 12px; height: 12px; }
</style>
</head>
<body>

  <section class="card card--front" aria-label="Business card front">
    <div class="wordmark">HARBOR <span class="wordmark__dot"></span> CREST</div>

    <div class="holder">
      <p class="holder__name">Liam Carter</p>
      <p class="holder__role">Director</p>
    </div>

    <div class="contact-frame"></div>
    <div class="contact-panel">
      <ul class="contact-list">
        <li>
          <svg viewBox="0 0 10 10"><path d="M1 3c0-1 1-2 4-2s4 1 4 2v1H7V3H3v1H1z M2 5h6l1 4H1z" fill="#1f2a30"/></svg>
          1300 555 014
        </li>
        <li>
          <svg viewBox="0 0 10 10"><rect x="2.5" y="0.5" width="5" height="9" rx="1" fill="none" stroke="#1f2a30"/><circle cx="5" cy="8" r="0.6" fill="#1f2a30"/></svg>
          +613 9555 0182
        </li>
        <li>
          <svg viewBox="0 0 10 10"><rect x="0.5" y="2" width="9" height="6" fill="#1f2a30"/><path d="M0.5 2l4.5 3.5L9.5 2" fill="none" stroke="#7ba43c"/></svg>
          support@harborcrest.com.au
        </li>
        <li>
          <svg viewBox="0 0 10 10"><circle cx="5" cy="5" r="4.3" fill="none" stroke="#1f2a30"/><ellipse cx="5" cy="5" rx="1.8" ry="4.3" fill="none" stroke="#1f2a30" stroke-width="0.8"/><path d="M0.7 5h8.6" stroke="#1f2a30" stroke-width="0.8"/></svg>
          www.harborcrest.com.au
        </li>
      </ul>
    </div>

    <div class="address-band">
      <address class="address">Level 2, 48 Wattle Street<br>Southbank VIC 3006</address>
      <svg viewBox="0 0 12 12"><path d="M6 1L1 6h1.5v5h3V8h1v3h3V6H11z" fill="#7ba43c"/></svg>
    </div>
  </section>

  <section class="card card--back" aria-label="Business card back">
    <div class="wordmark">HARBOR <span class="wordmark__dot"></span> CREST</div>
  </section>

</body>
</html>
```